Orvane Constructions Business card and Logo

We are a building company that would like our current logo design copied with the "Orvane Constructions" lines thicker.
We would also like our business cards copied with some minor copy changes. I have attached images of our logo and business cards.
We would like a standard size business card in landscape format rather than portrait.
On the back of the business card we would like a name added above the mobile number - "Remy Castellan"
Can I please get high res file of the logo and business cards at completion of redesign?

```html
<!DOCTYPE html>
<html lang="en">
<head>
<meta charset="utf-8">
<title>Orvane Constructions – Business Cards</title>
<link rel="stylesheet" href="https://fonts.googleapis.com/css2?family=Arimo&family=Libre+Baskerville:wght@400;700&display=swap">
<style>
  :root {
    --stage: #3b3b3b;
    --paper: #ffffff;
    --ink: #111111;
    --front-green: #2ddd00;
    --front-green-light: #45e41c;
    --back-green: #00ee00;
    --back-type: #8cff7a;
    --icon-blue: #2a9df4;
    --icon-green: #22dd00;
  }
  * { box-sizing: border-box; margin: 0; padding: 0; }
  html, body {
    width: 1200px; height: 900px; overflow: hidden;
    background: var(--stage);
  }
  .canvas { position: relative; width: 1200px; height: 900px; }

  .card {
    position: absolute;
    width: 540px; height: 316px;
    border-radius: 26px;
    overflow: hidden;
    background: var(--paper);
  }

  /* Front card */
  .card--front { left: 60px; top: 110px; display: flex; }
  .contact-column {
    width: 34%;
    padding: 34px 22px 0 26px;
    display: flex; flex-direction: column; align-items: center;
  }
  .contact-row {
    width: 100%;
    height: 80px;
    display: flex; flex-direction: column; align-items: center; justify-content: center;
    border-bottom: 4px solid var(--ink);
  }
  .contact-row:first-child { height: 66px; justify-content: flex-start; }
  .contact-name {
    font-family: "Libre Baskerville", serif;
    font-size: 12px; color: var(--ink); margin-top: 6px;
  }
  .contact-at {
    font-family: "Arimo", sans-serif;
    font-size: 34px; color: var(--icon-green); line-height: 1;
  }
  .brand-panel {
    position: relative; flex: 1;
    background: var(--front-green);
    display: flex; flex-direction: column; justify-content: center;
    padding-left: 52px;
  }
  .brand-panel__backdrop {
    position: absolute; inset: 0;
    background: linear-gradient(135deg, var(--front-green-light), var(--front-green) 60%);
  }
  .brand-panel__mark, .brand-panel__name {
    position: relative;
    font-family: "Libre Baskerville", serif;
    font-weight: 700; color: var(--paper);
  }
  .brand-panel__mark { font-size: 82px; line-height: 1; letter-spacing: 2px; }
  .brand-panel__name { font-size: 26px; margin-top: 8px; }

  /* Back card */
  .card--back { left: 620px; top: 480px; background: var(--back-green); }
  .back-brand {
    position: absolute; left: 56px; top: 40px;
    font-family: "Arimo", sans-serif; font-weight: 400; color: var(--back-type);
  }
  .back-brand__mark { font-size: 120px; line-height: 1; letter-spacing: 6px; }
  .back-brand__name { font-size: 36px; margin-top: 12px; }
  .back-strip {
    position: absolute; left: 0; right: 0; bottom: 0; height: 58px;
    background: var(--paper);
  }
</style>
</head>
<body>
<main class="canvas">

  <section class="card card--front" aria-label="Business card front">
    <div class="contact-column">
      <div class="contact-row">
        <svg class="icon-phone" width="28" height="30" viewBox="0 0 28 30" aria-hidden="true">
          <rect width="28" height="30" rx="4" fill="var(--icon-blue)"/>
          <path d="M10 7 q-4 8 2 16 l3 -2 -3-4 q-2 -3 0 -6 l3 -2 -3 -4z" fill="#fff"/>
        </svg>
        <span class="contact-name">Remy Castellan</span>
      </div>
      <div class="contact-row">
        <svg width="20" height="40" viewBox="0 0 20 40" aria-hidden="true">
          <path d="M2 6 Q10 -2 18 6 L13 38 Z" fill="var(--icon-green)"/>
        </svg>
      </div>
      <div class="contact-row">
        <span class="contact-at">@</span>
      </div>
    </div>
    <div class="brand-panel">
      <div class="brand-panel__backdrop" role="img" aria-label="Faint line drawing of a building interior in lighter green"></div>
      <div class="brand-panel__mark">OVC</div>
      <div class="brand-panel__name">Constructions</div>
    </div>
  </section>

  <section class="card card--back" aria-label="Business card back">
    <div class="back-brand">
      <div class="back-brand__mark">OVC</div>
      <div class="back-brand__name">Orvane Constructions</div>
    </div>
    <div class="back-strip"></div>
  </section>

</main>
</body>
</html>
```